依頼概要
■ 依頼の目的/概要

インターネットマーケティングのコンサルティング会社の名刺デザインを依頼させて頂きます。

■ 名刺に記載する情報

表面:会社名/役職/氏名/住所/電話/Fax/Mail/HP

裏面には、↓の3つの単語と、下記の文章(2行と1行。1行の方はキャッチコピーになりますが、まだ正式に決まってません。25文字程度になる予定です)をお願いします。
それぞれの位置はお任せします。

Simple Solution Satisfaction

シンプルな解決法で集客アップ、売上アップを実現。
最上級の満足を与えるインターネットマーケティングコンサルティング会社です。

〜を制するものは〜を制す

■ 名刺デザインへの要望

「シンプル」だけど、印象に残る「かっこいい」「クール」「スタイリッシュ」なデザインを希望します。
色は、白背景またはロゴ色に合わせた名刺にしたいと考えています。

添付のロゴを使用し、ロゴを目立つようにお願いします。
縦、横(91mm x 55mm)、どちらも見てみたいと思います。

添付ロゴはカラーと白黒があります。
表はカラーでお願いします。
裏は白黒で考えていますが、カラーの案でも可能です。

■ 納品ファイルの希望

イラストレーター形式および高画質jpg形式

(そのままインターネット上の名刺印刷業者に渡せば印刷してもらえる形式でお願いします。
http://new.quelmark.jp/ のデータ作業案内→データ作成ガイド などの形式)

■ 進め方

弊社の希望するイメージに近い提案を1つ(場合によって複数)選択させて頂きます。希望に近づけるために、修正要望を個別にさせて頂くこともあります。コンペ方式のため、修正後に当選されない場合も、どうかご了承ください。

■ その他/注意点

選択させて頂いた名刺デザインの著作権(財産権)等の扱いはBrivoto利用規約に従い、弊社に譲渡をお願いします。フォントや画像素材などを利用する場合は上記利用用途に使用できることを確認し、第三者の知的財産権等に注意して下さい。
ロゴが添付されてなかったので添付しました。
ロゴを添付しました。
■ 選んだ理由

裏面のインパクトが印象的でしたので決めました。

■ 提案者全員のお礼・コメント

たくさんのご提案ありがとうございました。
要望に応えてくださったデザインが多くて感謝しております。
また機会がありましたらよろしくお願い致します。

```html
<!DOCTYPE html>
<html lang="ja">
<head>
<meta charset="UTF-8">
<title>Nova Marketing Japan — Business Card</title>
<link rel="stylesheet" href="https://fonts.googleapis.com/css2?family=Noto+Serif+JP:wght@400;500&display=swap">
<style>
  :root {
    --backdrop: #eceeef;
    --card: #ffffff;
    --ink: #2f2f2f;
    --ink-soft: #555555;
    --accent: #2b7bc6;
    --brand: #1f3766;
    --mark: #2a66b3;
  }
  * { margin: 0; padding: 0; box-sizing: border-box; }
  html, body {
    width: 844px;
    height: 1200px;
    overflow: hidden;
    background: var(--backdrop);
  }
  .card {
    position: absolute;
    left: 92px;
    top: 54px;
    width: 660px;
    height: 1092px;
    background: var(--card);
    font-family: "Noto Serif JP", serif;
    color: var(--ink);
  }
  .profile {
    position: absolute;
    left: 72px;
    top: 226px;
  }
  .profile__title {
    font-size: 26px;
    letter-spacing: 0.04em;
  }
  .profile__name {
    margin-top: 8px;
    font-size: 52px;
    font-weight: 400;
    letter-spacing: 0.08em;
    line-height: 1.2;
  }
  .profile__romaji {
    margin-top: 10px;
    font-size: 20px;
    color: var(--ink-soft);
  }
  .contact {
    position: absolute;
    left: 72px;
    top: 412px;
    font-size: 21px;
    line-height: 1.62;
  }
  .contact__company {
    font-size: 26px;
    color: var(--accent);
    letter-spacing: 0.05em;
    margin-bottom: 8px;
  }
  .brand {
    position: absolute;
    left: 0;
    top: 690px;
    width: 100%;
    text-align: center;
  }
  .brand__dot {
    display: block;
    margin: 0 auto;
  }
  .brand__name {
    margin-top: 70px;
    font-size: 46px;
    font-weight: 400;
    color: var(--brand);
    letter-spacing: 0.04em;
  }
</style>
</head>
<body>
  <main class="card">
    <section class="profile">
      <p class="profile__title">代表取締役</p>
      <h1 class="profile__name">佐藤 健一</h1>
      <p class="profile__romaji">Kenichi Sato</p>
    </section>

    <address class="contact" style="font-style: normal;">
      <p class="contact__company">ノヴァ マーケティング ジャパン</p>
      <p>〒145-0872 東京都港南区青葉町3-8-15</p>
      <p>TEL 03-4821-7096&nbsp;&nbsp;FAX 03-4821-7097</p>
      <p>E-mail hello@novamkjapan.jp</p>
      <p>http://novamkjapan.jp</p>
    </address>

    <div class="brand">
      <svg class="brand__dot" width="180" height="180" viewBox="0 0 180 180" aria-hidden="true">
        <circle cx="90" cy="90" r="86" fill="var(--mark)"/>
      </svg>
      <p class="brand__name">Nova Marketing Japan</p>
    </div>
  </main>
</body>
</html>
```